Email Signature

We are looking for creative email signature for our company. Please find attached the logo of our company for your reference. now we understand there isn't much can be done with email signature but we are looking for out of the box designs. Nothing specific in mind

Please insert fake numbers, website and/or address, etc just to showcase the designs. once the design is chosen we will provide the actual details.
Updates

Dear All,

We wouldlike to extend our apology for not being able to provide feedbacks to everysingle design. We were extremely busy and we have multiple contests opensimultaneously which makes the process harder. However, thank you all for theefforts you have put into this contest. We have received anoverwhelming quality responses & it has been a very difficult task tochoose just one, we easily Loved at least several designs...

Thanksagain for participating, we wish you all success in your design ventures.

Kindregards,

KLC Team

Industry/Entity Type

It Company

```html
<!DOCTYPE html>
<html lang="en">
<head>
<meta charset="utf-8">
<title>Kitchen Lantern Co – Email Signature</title>
<link href="https://fonts.googleapis.com/css2?family=Nunito:wght@600;700;800&display=swap" rel="stylesheet">
<style>
  :root {
    --page-bg: #ffffff;
    --card-bg: #ffffff;
    --ink-grey: #5f5f5f;
    --ink-dark: #3a3a3a;
    --rule: #6d6d6d;
    --brand-blue: #1b86de;
    --tag-blue: #1d62ad;
    --string: #9a9a9a;
  }
  * { margin: 0; padding: 0; box-sizing: border-box; }
  html, body {
    width: 1200px; height: 933px; overflow: hidden;
    background: var(--page-bg);
    font-family: "Nunito", sans-serif;
  }
  .signature {
    position: absolute; left: 21px; top: 200px;
    width: 1159px; height: 530px;
    background: var(--card-bg);
    box-shadow: 4px 6px 8px rgba(0,0,0,0.35);
  }
  .person {
    position: absolute; left: 182px; top: 42px;
    color: var(--ink-grey); font-weight: 700;
    font-size: 41px; line-height: 54px;
  }
  .rule {
    position: absolute; left: 182px; width: 794px; height: 2px;
    background: var(--rule);
  }
  .rule.top { top: 163px; }
  .rule.bottom { top: 497px; }
  .brand {
    position: absolute; left: 182px; top: 190px; width: 794px;
    text-align: center;
    font-size: 86px; font-weight: 800; line-height: 120px;
    color: var(--brand-blue); letter-spacing: -1px;
  }
  .tags { position: absolute; left: 0; top: 0; width: 1159px; height: 530px; }
  .contact {
    position: absolute; left: 195px; top: 448px;
    display: flex; align-items: center;
    font-size: 16px; font-weight: 600; color: var(--ink-dark);
  }
  .contact span { padding: 0 12px; border-left: 3px solid var(--brand-blue); line-height: 26px; }
  .contact span:first-child { border-left: none; padding-left: 0; }
</style>
</head>
<body>
  <div class="signature">
    <div class="person">
      <p class="person-name">Samir Haddad</p>
      <p class="person-role">Art Diretor</p>
    </div>
    <div class="rule top"></div>

    <p class="brand">Kitchen Lantern</p>

    <svg class="tags" viewBox="0 0 1159 530" aria-hidden="true">
      <g stroke="var(--string)" stroke-width="1.5">
        <line x1="255" y1="310" x2="255" y2="386"/>
        <line x1="394" y1="310" x2="394" y2="392"/>
        <line x1="559" y1="310" x2="559" y2="386"/>
        <line x1="730" y1="310" x2="730" y2="382"/>
      </g>
      <!-- phone tag -->
      <g transform="translate(233 384)">
        <rect width="44" height="44" rx="3" fill="var(--tag-blue)" stroke="#c9d6e6" stroke-width="2"/>
        <path d="M16 12 q-4 2 -2 9 q3 8 10 11 q4 1 6 -2 l-4 -4 l-3 2 q-4 -2 -6 -7 l2 -3 z" fill="#fff"/>
      </g>
      <!-- mail tag -->
      <g transform="translate(372 390)">
        <rect width="44" height="44" rx="3" fill="var(--tag-blue)" stroke="#c9d6e6" stroke-width="2"/>
        <rect x="11" y="14" width="22" height="15" fill="#fff"/>
        <path d="M11 14 l11 9 l11 -9" fill="none" stroke="var(--tag-blue)" stroke-width="2"/>
      </g>
      <!-- web tag -->
      <g transform="translate(537 384)">
        <rect width="44" height="44" rx="3" fill="var(--tag-blue)" stroke="#c9d6e6" stroke-width="2"/>
        <circle cx="22" cy="22" r="9" fill="none" stroke="#fff" stroke-width="2"/>
        <path d="M13 22 h18 M22 13 v18 M16 16 q6 3 12 0 M16 28 q6 -3 12 0" fill="none" stroke="#fff" stroke-width="1.5"/>
      </g>
      <!-- address tag -->
      <g transform="translate(708 380)">
        <rect width="44" height="44" rx="3" fill="var(--tag-blue)" stroke="#c9d6e6" stroke-width="2"/>
        <path d="M11 23 l11 -10 l11 10 M14 21 v11 h16 v-11" fill="none" stroke="#fff" stroke-width="2.5"/>
        <rect x="19" y="25" width="6" height="7" fill="#fff"/>
      </g>
    </svg>

    <p class="contact">
      <span>(00) 1234-5678</span>
      <span>info@kitchenlantern.com</span>
      <span>www.kitchenlantern.com</span>
      <span>Your address goes here</span>
    </p>
    <div class="rule bottom"></div>
  </div>
</body>
</html>
```